Painting services company needs a DL brochure about their services

We need a brochure describing our painting services including our logo and photos of work. The final design needs to be colourful, vibrant, and targeted to schools, aged care, commercial property maintenance clients.

```html
<!DOCTYPE html>
<html lang="en">
<head>
<meta charset="utf-8">
<title>Brightcoat Painters – DL Brochure</title>
<link href="https://fonts.googleapis.com/css2?family=Oswald:wght@600;700&family=Montserrat:wght@400;500;600;700&display=swap" rel="stylesheet">
<style>
  :root{
    --brand-blue:#0d4a9b;
    --brand-yellow:#f7e24a;
    --paper:#ffffff;
    --ink:#2a2a2a;
    --backdrop:#8d8d8d;
    --photo-sky:#8fa2ea;
    --photo-wall:#4a4d57;
    --photo-plant:#9ea9b8;
    --photo-shop:#b07a5a;
  }
  *{box-sizing:border-box;margin:0;padding:0}
  html,body{width:1200px;height:1200px;overflow:hidden}
  body{background:var(--backdrop);font-family:"Montserrat",sans-serif;color:var(--ink);position:relative}
  .flyer{position:absolute;top:70px;width:500px;height:1060px;background:var(--paper);padding:14px;display:flex;flex-direction:column}
  .flyer--front{left:60px}
  .flyer--back{left:640px}

  /* front */
  .hero-photo{height:440px;background:linear-gradient(180deg,var(--photo-sky) 0%,#b9c4f0 45%,var(--photo-wall) 60%,#3a3c44 100%);position:relative}
  .brand-mark{position:absolute;top:40px;left:110px;width:160px;height:120px;background:var(--paper);display:flex;align-items:center;justify-content:center;text-align:center;padding:10px;font-weight:700;font-size:22px;line-height:1.15;color:var(--brand-blue)}
  .title-band{background:var(--brand-blue);padding:18px 26px 20px;margin:0 -14px}
  .title-band__lead{font-family:"Oswald",sans-serif;font-weight:700;font-size:40px;line-height:1;color:var(--paper);text-transform:uppercase}
  .title-band__main{font-family:"Oswald",sans-serif;font-weight:700;font-size:74px;line-height:1;color:var(--brand-yellow);text-transform:uppercase}
  .title-band__sub{font-size:19px;font-weight:500;color:var(--paper);margin-top:6px}
  .intro{font-size:14px;font-weight:600;line-height:1.35;padding:16px 26px 12px;color:var(--ink)}
  .highlight{background:var(--brand-yellow);color:var(--brand-blue);font-weight:700;font-size:19px;line-height:1.2;text-transform:uppercase;padding:12px 26px;margin:0 10px}
  .body-copy{font-size:13.5px;line-height:1.55;text-align:justify;padding:16px 26px;flex:1}
  .footer-band{background:var(--brand-blue);color:var(--paper);text-align:center;font-size:15px;font-weight:500;letter-spacing:.5px;padding:22px 10px;margin:0 -14px -14px}

  /* back */
  .collage{height:440px;display:grid;grid-template-columns:1fr 1fr;grid-template-rows:250px 1fr;gap:4px}
  .collage__plant{grid-column:1/3;background:linear-gradient(160deg,#5a5f6a,var(--photo-plant) 50%,#d6d9de)}
  .collage__gym{background:linear-gradient(180deg,#6f8088,#a8b3b6 60%,#5b6566)}
  .collage__shop{background:linear-gradient(180deg,#e8c9a8,var(--photo-shop) 60%,#7e3c3a)}
  .services-band{background:var(--brand-blue);color:var(--brand-yellow);font-family:"Oswald",sans-serif;font-weight:700;font-size:28px;text-transform:uppercase;text-align:center;padding:10px;margin:0 -14px}
  .services{padding:16px 18px 8px;flex:1;display:flex;flex-direction:column;gap:14px}
  .service-group__title{color:var(--brand-blue);font-weight:700;font-size:14.5px;margin-bottom:5px}
  .service-group__cols{display:grid;grid-template-columns:1fr 1fr;gap:0 18px}
  .service-list{list-style:none}
  .service-list li{display:flex;gap:7px;font-size:13px;line-height:1.3;margin-bottom:4px}
  .tick{flex:0 0 11px;width:11px;height:11px;margin-top:3px}
  .call-band{background:var(--brand-yellow);color:var(--brand-blue);font-weight:700;font-size:22px;display:flex;justify-content:space-between;align-items:center;padding:12px 22px;margin:0 10px}
  .call-band__phone{display:flex;align-items:center;gap:6px}
</style>
</head>
<body>
<svg width="0" height="0" style="position:absolute">
  <symbol id="tick" viewBox="0 0 12 12">
    <rect x="0.75" y="0.75" width="10.5" height="10.5" fill="none" stroke="#0d4a9b" stroke-width="1.2"/>
    <path d="M3 6.2l2 2 4-4.5" fill="none" stroke="#0d4a9b" stroke-width="1.5"/>
  </symbol>
</svg>

<section class="flyer flyer--front">
  <div class="hero-photo" role="img" aria-label="Photo of a freshly painted commercial supermarket building with trees under a blue sky">
    <div class="brand-mark">Brightcoat Painters</div>
  </div>
  <div class="title-band">
    <div class="title-band__lead">Friendly Painting</div>
    <div class="title-band__main">Contractors</div>
    <div class="title-band__sub">Commercial Painters in Australia</div>
  </div>
  <p class="intro">Brightcoat Painters is a specialist commercial painting, decorating and protective coatings application company servicing all states of Australia</p>
  <p class="highlight">We are a family-run business with over 40 years' experience</p>
  <p class="body-copy">We provide a full range of painting, decorating and protective coatings services through specialised divisions. This is the best way to guarantee that our clients are getting the best level of customer service possible from the enquiry &amp; quotation to the provision of the right staff with the right skills and attitude to carry out the required preparation and application.</p>
  <div class="footer-band">www.brightcoatpainters.com.au</div>
</section>

<section class="flyer flyer--back">
  <div class="collage">
    <div class="collage__plant" role="img" aria-label="Photo of painted industrial tanks and pipework"></div>
    <div class="collage__gym" role="img" aria-label="Photo of a painted gym interior with equipment"></div>
    <div class="collage__shop" role="img" aria-label="Photo of a painted retail store interior"></div>
  </div>
  <div class="services-band">Specialist Painting Contractors</div>
  <div class="services">
    <div class="service-group">
      <h3 class="service-group__title">Commercial &amp; industrial painting services</h3>
      <div class="service-group__cols">
        <ul class="service-list">
          <li><svg class="tick"><use href="#tick"/></svg>Pressure cleaning of building facades</li>
          <li><svg class="tick"><use href="#tick"/></svg>On-site spray painting</li>
          <li><svg class="tick"><use href="#tick"/></svg>Texture coatings</li>
          <li><svg class="tick"><use href="#tick"/></svg>After-hours &amp; weekends available</li>
        </ul>
        <ul class="service-list">
          <li><svg class="tick"><use href="#tick"/></svg>Painting of broad areas and trim to commercial interiors and exteriors</li>
          <li><svg class="tick"><use href="#tick"/></svg>Corrosion repairs and protective coatings for steel</li>
        </ul>
      </div>
    </div>
    <div class="service-group">
      <h3 class="service-group__title">Floor preparation and coating services</h3>
      <div class="service-group__cols">
        <ul class="service-list">
          <li><svg class="tick"><use href="#tick"/></svg>Diamond grinding</li>
          <li><svg class="tick"><use href="#tick"/></svg>Shot blasting</li>
          <li><svg class="tick"><use href="#tick"/></svg>Anti-slip coatings</li>
          <li><svg class="tick"><use href="#tick"/></svg>Glue &amp; surface removal</li>
        </ul>
        <ul class="service-list">
          <li><svg class="tick"><use href="#tick"/></svg>Epoxy &amp; polyurethane coatings</li>
          <li><svg class="tick"><use href="#tick"/></svg>Epoxy floors for warehouse &amp; workshop</li>
        </ul>
      </div>
    </div>
    <div class="service-group">
      <h3 class="service-group__title">New construction painting services</h3>
      <div class="service-group__cols">
        <ul class="service-list">
          <li><svg class="tick"><use href="#tick"/></svg>Painting of new buildings</li>
          <li><svg class="tick"><use href="#tick"/></svg>Internals &amp; externals</li>
        </ul>
        <ul class="service-list">
          <li><svg class="tick"><use href="#tick"/></svg>Spray painting and texture coatings</li>
        </ul>
      </div>
    </div>
  </div>
  <div class="call-band">
    <span>CALL US TODAY!</span>
    <span class="call-band__phone">
      <svg width="20" height="20" viewBox="0 0 24 24" aria-hidden="true"><path d="M6.6 10.8a15.1 15.1 0 006.6 6.6l2.2-2.2a1 1 0 011-.25 11.4 11.4 0 003.6.57 1 1 0 011 1V20a1 1 0 01-1 1A17 17 0 013 4a1 1 0 011-1h3.5a1 1 0 011 1c0 1.25.2 2.45.57 3.57a1 1 0 01-.25 1z" fill="#0d4a9b"/></svg>
      1300 555 018
    </span>
  </div>
  <div class="footer-band">www.brightcoatpainters.com.au</div>
</section>
</body>
</html>
```